Business Card & Stationary
Harbor Lane Finanical
Project: Business Card & Stationary
Business Card & Stationary - Financial Services
Creative Brief
Simple
Gordon Pelling
President
274 W. Larkspur Blvd. Suite 2260 Chicago, IL 60614
gpelling@harborlanefin.com
www.harborlanefin.com
The stationary should also be converted into a template for Word. We will get the business cards and envelopes printed but probably just use a laser printer for the stationary.
Some element of our logo .... make it look nice.

```html
<!DOCTYPE html>
<html lang="en">
<head>
<meta charset="utf-8">
<title>Harbor Lane Finanical – Stationery</title>
<link rel="stylesheet" href="https://fonts.googleapis.com/css2?family=Cormorant+Garamond:wght@600&family=Open+Sans:wght@400;600&display=swap">
<style>
:root{
  --bg-light:#6a6a6a;
  --bg-dark:#2e2e2e;
  --paper:#ffffff;
  --paper-shade:#eeeeec;
  --olive:#7a8b2e;
  --olive-dark:#5f6e20;
  --charcoal:#4a4642;
  --ink:#555555;
  --label:#d8d8d8;
  --faint:#f1f3ea;
}
*{margin:0;padding:0;box-sizing:border-box}
html,body{width:1200px;height:444px;overflow:hidden}
body{
  position:relative;
  background:radial-gradient(ellipse at 50% 45%,var(--bg-light),var(--bg-dark) 80%);
  font-family:"Open Sans",Arial,sans-serif;color:var(--ink);
}
.piece{position:absolute;background:var(--paper);box-shadow:0 3px 8px rgba(0,0,0,.45)}
.label{position:absolute;font-size:7px;color:var(--label);text-align:center}
.mark{display:inline-block;width:14px;height:14px;background:var(--olive);vertical-align:middle}
.brand{font-family:"Cormorant Garamond",Georgia,serif;font-weight:600;color:var(--olive);text-transform:uppercase;letter-spacing:.5px;line-height:1.1}
.small{font-size:5px;line-height:1.5}

/* business cards */
.card{left:18px;width:166px;height:92px}
.card-front{top:150px}
.card-front .brand{position:absolute;left:10px;top:10px;font-size:8px}
.card-front .name-band{position:absolute;left:0;right:0;top:40px;height:10px;background:var(--olive);color:var(--paper);font-size:5.5px;font-weight:600;padding:2px 8px}
.card-front .contact{position:absolute;left:10px;top:56px}
.card-front .web{position:absolute;left:0;right:0;bottom:0;height:10px;background:var(--olive-dark);color:var(--paper);font-size:5px;padding:2px 8px}
.card-back-green{top:262px;background:var(--olive)}
.card-back-green .brand{position:absolute;left:12px;top:18px;font-size:9px;color:var(--paper)}
.card-back-green .web{position:absolute;left:12px;bottom:10px;font-size:5px;color:var(--paper)}
.card-back-white{top:366px;height:70px}
.card-back-white .brand{position:absolute;left:12px;top:16px;font-size:9px}
.card-back-white .strip{position:absolute;left:0;right:0;bottom:0;height:8px;background:var(--olive)}

/* letterheads */
.letterhead{top:20px;width:232px;height:392px}
.letterhead-1{left:206px}
.letterhead-2{left:452px}
.letterhead .brand{position:absolute;left:16px;top:14px;font-size:7.5px}
.letterhead .contact{position:absolute;right:16px;top:14px;text-align:left}
.letterhead .ghost{position:absolute;left:28px;top:120px;width:150px;height:150px;background:var(--faint)}
.letterhead .footer{position:absolute;left:0;right:0;bottom:0;height:8px;background:var(--olive)}
.letterhead .rule{position:absolute;left:16px;right:16px;top:44px;height:1px;background:var(--olive)}

/* envelopes */
.envelope{left:738px;width:444px;height:82px;overflow:hidden}
.env-1{top:40px}
.env-2{top:130px}
.env-3{top:220px}
.env-4{top:320px;height:100px}
.envelope svg{position:absolute;left:0;top:0}
.envelope .brand{position:absolute;font-size:8px}
.env-1 .brand,.env-2 .brand{left:206px;top:30px;font-size:7px;color:var(--paper)}
.env-4 .brand{left:14px;top:12px;font-size:9px}
.env-4 .contact{position:absolute;left:14px;top:36px}
</style>
</head>
<body>

<!-- business cards -->
<div class="piece card card-front">
  <div class="brand"><span class="mark"></span> Harbor Lane Finanical</div>
  <div class="name-band">Gordon Pelling &nbsp;·&nbsp; President</div>
  <div class="contact small">274 W. Larkspur Blvd. Suite 2260<br>Chicago, IL 60614<br>gpelling@harborlanefin.com</div>
  <div class="web">www.harborlanefin.com</div>
</div>
<div class="label" style="left:18px;top:244px;width:166px">Front Card</div>

<div class="piece card card-back-green">
  <div class="brand"><span class="mark" style="background:var(--paper)"></span> Harbor Lane Finanical</div>
  <div class="web">www.harborlanefin.com</div>
</div>
<div class="label" style="left:18px;top:356px;width:166px">Back Card 01</div>

<div class="piece card card-back-white">
  <div class="brand"><span class="mark"></span> Harbor Lane Finanical</div>
  <div class="strip"></div>
</div>
<div class="label" style="left:18px;top:437px;width:166px">Back Card 02</div>

<!-- letterheads -->
<div class="piece letterhead letterhead-1">
  <div class="brand"><span class="mark"></span><br>Harbor Lane Finanical</div>
  <div class="contact small">274 W. Larkspur Blvd. Suite 2260<br>Chicago, IL 60614<br>gpelling@harborlanefin.com<br>www.harborlanefin.com</div>
  <div class="ghost"></div>
  <div class="footer"></div>
</div>
<div class="label" style="left:206px;top:416px;width:232px">Letterhead Option 01</div>

<div class="piece letterhead letterhead-2">
  <div class="brand"><span class="mark"></span><br>Harbor Lane Finanical</div>
  <div class="contact small">274 W. Larkspur Blvd. Suite 2260<br>Chicago, IL 60614<br>gpelling@harborlanefin.com<br>www.harborlanefin.com</div>
  <div class="rule"></div>
  <div class="ghost"></div>
  <div class="footer" style="height:14px"></div>
</div>
<div class="label" style="left:452px;top:416px;width:232px">Letterhead Option 02</div>

<!-- envelopes -->
<div class="label" style="left:738px;top:26px;width:444px;text-align:right">Envelope Front &amp; Back</div>

<div class="piece envelope env-1">
  <svg width="444" height="82" viewBox="0 0 444 82"><polygon points="0,0 444,0 222,54" fill="var(--olive)"/></svg>
  <div class="brand"><span class="mark" style="background:var(--paper)"></span></div>
</div>

<div class="piece envelope env-2">
  <svg width="444" height="82" viewBox="0 0 444 82"><polygon points="0,0 444,0 222,54" fill="var(--charcoal)"/></svg>
  <div class="brand"><span class="mark" style="background:var(--olive)"></span></div>
</div>

<div class="piece envelope env-3">
  <svg width="444" height="82" viewBox="0 0 444 82">
    <polygon points="0,0 444,0 222,50" fill="var(--paper-shade)"/>
    <polyline points="0,82 222,36 444,82" fill="none" stroke="#d4d4d0" stroke-width="1"/>
    <rect x="0" y="78" width="444" height="4" fill="var(--olive)"/>
  </svg>
</div>

<div class="piece envelope env-4">
  <div class="brand"><span class="mark"></span> Harbor Lane Finanical</div>
  <div class="contact small">274 W. Larkspur Blvd. Suite 2260<br>Chicago, IL 60614</div>
  <svg width="444" height="100" viewBox="0 0 444 100"><rect x="0" y="94" width="444" height="6" fill="var(--olive)"/></svg>
</div>

</body>
</html>
```